Fenwick and Ostrander Postcard Design

Greetings!
Lawyers hire me as an expert witness. They take a gamble on hiring me in hopes of winning their case.
This postcard will be printed in jumbo size through Printoria. The design must meet these specifications:

Full Bleed Size (starting document size)
11.12" x 6.12"
282 x 155 mm
3335 x 1835 pixels
* Finished artwork should use the full bleed dimensions for best results.
Document Trim Size (final size after being cut)
11.00" x 6.00"
279 x 152 mm
3300 x 1800 pixels
* Please be sure to keep all text and photos within the safe cutting margin.
Resolution
300 DPI
Visit Printoria for more details or to download a design template:
https://www.printoria-example.com/product-presentation-info.aspx?productPresentationId=2741#
https://www.printoria-example.com/vp/ns/propath/UploadResources.aspx?selectedTab=0?pfid=KRT&pf_id=KRT&xnav=product-page#FileFormats

1. The postcard will have a Blank Backside.
2. I like a black, white and red color theme with a serious legalistic font.
3. In regards to color theme, see https://www.mailerzest-example.com/designs/security-system-postcards/#security-system-postcards-4
4. 8 preferred background images in alphabetical order from favorite to least favorite, but all are great:
a. https://files-example.net/f/s!QwZr83TbLm2uvoxkN7HdY5pW1sgjre
5. Header Text:
a. (line 1) Dr. R.T. Ostrander, Psy.D., ABPP
b. (lines 2 and 3) Psychological Evaluator, Board-Certified Forensic Psychologist and National Expert Witness
c. (Line 4 in bold and more prominent than text in lines 1-3) 4 Signs of a Proficient & Credible Psyc. Expert
6. View this checklist image for inspiration, https://lnkbox-example.net/images/9TqWm3 and use the following text within such a checklist image:
7. Board Certified by the Continental Council of Courtroom Behavioral Science (CCCBS)?
Yes, I'm Board Certified. This mark of proficiency in forensic psychology is recognized by judicial decisions, statutes and regulations.
8. Fellow of the Cont. College of Courtroom Behavioralists?
Yes, I'm a CCCB Fellow, along with some of the field's most prominent leaders comprising the academic arm of the CCCBS.
9. A Recognized Leader Amongst Other Experts?
I’m the 2018 duly elected President of the Empire Region Mental Health Guild Section on Courtroom Behavior, and a Board Member of the National Practitioners Council for Youth Welfare Protection.
10. Positioned in Roles of Trust and Neutrality by Judges?
Yes, I work as an in-house Harbor County Domestic Tribunal mental-health expert in proceedings regarding competency, imminent risk, sentencing, custody, child maltreatment and TPR.
11. The following should be prominent along the bottom:
12. BOOK A LUNCH & LEARN AT YOUR OFFICE
Visit http://offer.benchwise-example.com Call 212-555-0147
Designer: This call to action (CTA) for #12 needs to pop off of the page. It needs to draw the reader's eye. It needs depth, like the way a CTA button looks like on a website. Play around w/ idea to accomplish this (e.g., adding badges, icons, shapes, a picture, an image of someone presenting it, etc).
13. List my areas of specialization somewhere
• CPS & Matrimonial Issues
• Competency
• Juvenile Delinquency
• Criminal Sentencing
• Personal Injury and Civil Rights
• Immigration
• Fitness for Duty, SSD and Workers Comp
• Sex-Offenders
• IME and Neuropsychological Testing
• Behind-The-Scenes Consulting on A Contingency Fee
• Low-Price Initial Screening Evaluations
• Therapy Services & Programs for Litigants
14. Put this test somewhere and keep it subtle: I recognize the importance of your work. You can trust my assistance.
15. Put this in fine print somewhere (can be 2 lines): Fenwick and Ostrander, LLC. 2018 New York Licensed Psychologist Lic. # 047213 - New Jersey Licensed Psychologist Lic. # 72K400915300

Target Market(s)

Lawyers

Industry/Entity Type

Hire

Font styles to use
Serif

Colors
ec1f27
ffffff

Requirements
Must have
• An awesome call to action. If the CTA doesn't catch the eye, then it won't work. The point of this postcard is to get them to that website so I can capture their email address. Anything else is a secondary gain. Consider 3-d design elements to give it pop and depth.
Should not have
• There's a big difference between a red rectangle and a red button on a website that has that 3d quality. This postcard has a lot of words. It can easily become just a bunch of text on a colorful piece of paper w/ a pic. Avoid this by segmenting the space, layering Diff color text on Diff color background and incorporating 3d design elements and shapes.

```html
<!DOCTYPE html>
<html lang="en">
<head>
<meta charset="utf-8">
<title>Fenwick and Ostrander Postcard</title>
<link href="https://fonts.googleapis.com/css2?family=Montserrat:ital,wght@0,400;0,500;0,600;0,700;0,800;1,400;1,500&display=swap" rel="stylesheet">
<style>
  :root {
    --red: #ec1f27;
    --red-dark: #a8121a;
    --red-light: #ff4a50;
    --black: #000000;
    --white: #ffffff;
    --page: #ececec;
    --ink: #111111;
    --muted: #4a4844;
    --stone-dark: #8d8a84;
    --stone-mid: #c9c5bd;
    --stone-light: #f3f2f0;
  }
  * { margin: 0; padding: 0; box-sizing: border-box; }
  html, body {
    width: 1200px; height: 1000px; overflow: hidden;
    background: var(--page);
    font-family: "Montserrat", sans-serif;
  }
  .postcard {
    position: absolute; left: 67px; top: 210px;
    width: 1076px; height: 592px;
    background: var(--white);
  }
  .side-panel {
    position: absolute; left: 0; top: 0;
    width: 389px; height: 592px;
    background: var(--black);
  }
  .hero-image {
    position: absolute; left: 389px; top: 0;
    width: 687px; height: 428px;
    background: linear-gradient(100deg, var(--stone-dark) 0%, var(--stone-mid) 35%, #dcd9d3 60%, var(--stone-light) 85%, #f6f6f6 100%);
  }
  .trust-line {
    position: absolute; right: 16px; top: 404px;
    font-size: 11px; font-style: italic; font-weight: 500;
    color: var(--muted);
  }
  .name-block {
    position: absolute; left: 30px; top: 27px;
    width: 425px; height: 96px;
    border: 1.5px solid var(--red);
    background: rgba(0,0,0,0.82);
    padding: 11px 0 0 18px;
    color: var(--white);
  }
  .name-block .doctor { font-size: 23px; font-weight: 700; letter-spacing: 0.2px; }
  .name-block .title { margin-top: 8px; font-size: 14px; font-weight: 500; line-height: 18px; }
  .checklist-heading {
    position: absolute; left: 20px; top: 141px; width: 350px;
    color: var(--red); font-size: 15px; font-weight: 700; line-height: 18px;
  }
  .checklist {
    position: absolute; left: 22px; top: 183px; width: 340px;
    list-style: none; color: var(--white);
  }
  .checklist li {
    position: relative; padding-left: 19px;
    font-size: 11px; line-height: 15px; text-align: justify;
    margin-bottom: 10px;
  }
  .checklist li svg { position: absolute; left: 0; top: 2px; }
  .checklist .question { font-weight: 700; }
  .checklist .answer { font-style: italic; }
  .cta-button {
    position: absolute; left: 20px; top: 498px;
    width: 349px; height: 82px;
    border-radius: 10px;
    background: linear-gradient(180deg, var(--red-light) 0%, var(--red) 45%, var(--red-dark) 100%);
    border-top: 1px solid rgba(255,255,255,0.45);
    box-shadow: 0 5px 0 #6e0b10, 0 9px 14px rgba(236,31,39,0.35);
    text-align: center; color: var(--white);
    padding-top: 9px;
  }
  .cta-button .cta-title {
    font-size: 14px; font-weight: 800; letter-spacing: 0.4px;
    text-shadow: 0 1px 2px rgba(0,0,0,0.45);
  }
  .cta-button .cta-contact {
    margin-top: 6px;
    font-size: 12.5px; font-weight: 700; line-height: 17px;
  }
  .cta-button .cta-contact .accent { color: #ffe7e8; text-decoration: underline; }
  .specialties {
    position: absolute; left: 389px; top: 428px;
    width: 687px; height: 124px;
    background: var(--red); color: var(--white);
    padding: 9px 14px 0 14px;
  }
  .specialties h2 { font-size: 17px; font-weight: 700; letter-spacing: 0.3px; margin-bottom: 4px; }
  .specialties p { font-size: 11.6px; font-weight: 500; line-height: 16.3px; text-transform: uppercase; }
  .fine-print {
    position: absolute; left: 389px; top: 552px;
    width: 687px; height: 40px;
    padding-top: 6px;
    text-align: center; color: var(--ink);
    font-size: 10px; line-height: 13px; font-weight: 500; text-transform: uppercase;
  }
  .fine-print strong { font-weight: 700; }
</style>
</head>
<body>
  <div class="postcard">
    <div class="side-panel"></div>
    <div class="hero-image" role="img" aria-label="Photograph of a classical marble colonnade with Ionic columns curving around a domed building against a white sky"></div>
    <p class="trust-line">I recognize the importance of your work. You can trust my assistance.</p>

    <div class="name-block">
      <div class="doctor">Dr. R.T. Ostrander, Psy.D., ABPP</div>
      <div class="title">Psychological Evaluator, Board-Certified Forensic<br>Psychologist &amp; National Expert Witness</div>
    </div>

    <h1 class="checklist-heading">4 Signs of a Proficient &amp; Credible<br>Psyc. Expert</h1>

    <ul class="checklist">
      <li>
        <svg width="10" height="10" viewBox="0 0 10 10"><circle cx="5" cy="5" r="4.2" fill="none" stroke="#ec1f27" stroke-width="1.2"/><path d="M3 5.1 L4.5 6.5 L7.2 3.6" fill="none" stroke="#ec1f27" stroke-width="1.2"/></svg>
        <span class="question">Board Certified by the Continental Council of Courtroom Behavioral Science (CCCBS)?</span>
        <span class="answer">Yes, I'm Board Certified. This mark of proficiency in forensic psychology is recognized by judicial decisions, statutes and regulations.</span>
      </li>
      <li>
        <svg width="10" height="10" viewBox="0 0 10 10"><circle cx="5" cy="5" r="4.2" fill="none" stroke="#ec1f27" stroke-width="1.2"/><path d="M3 5.1 L4.5 6.5 L7.2 3.6" fill="none" stroke="#ec1f27" stroke-width="1.2"/></svg>
        <span class="question">Fellow of the Cont. College of Courtroom Behavioralists?</span>
        <span class="answer">Yes, I'm a CCCB Fellow, along with some of the field's most prominent leaders, comprising the academic arm of the CCCBS.</span>
      </li>
      <li>
        <svg width="10" height="10" viewBox="0 0 10 10"><circle cx="5" cy="5" r="4.2" fill="none" stroke="#ec1f27" stroke-width="1.2"/><path d="M3 5.1 L4.5 6.5 L7.2 3.6" fill="none" stroke="#ec1f27" stroke-width="1.2"/></svg>
        <span class="question">A Recognized Leader Amongst Other Experts?</span>
        <span class="answer">I'm the 2018 duly elected President of the Empire Region Mental Health Guild Section on Courtroom Behavior, and a Board Member of the National Practitioners Council for Youth Welfare Protection.</span>
      </li>
      <li>
        <svg width="10" height="10" viewBox="0 0 10 10"><circle cx="5" cy="5" r="4.2" fill="none" stroke="#ec1f27" stroke-width="1.2"/><path d="M3 5.1 L4.5 6.5 L7.2 3.6" fill="none" stroke="#ec1f27" stroke-width="1.2"/></svg>
        <span class="question">Positioned in Roles of Trust and Neutrality by Judges?</span>
        <span class="answer">Yes, I'm an in-house Harbor County Domestic Tribunal mental-health expert for proceedings regarding competency, imminent risk, sentencing, custody, child maltreatment and TPR.</span>
      </li>
    </ul>

    <div class="cta-button">
      <div class="cta-title">BOOK A LUNCH &amp; LEARN AT YOUR OFFICE</div>
      <div class="cta-contact">
        Visit <span class="accent">http://offer.benchwise-example.com</span><br>
        or Call 212-555-0147
      </div>
    </div>

    <section class="specialties">
      <h2>AREAS OF SPECIALIZATION</h2>
      <p>CPS &amp;Matrimonial Issues &nbsp;|&nbsp; Competency &nbsp;|&nbsp; Juvenile Delinquency &nbsp;|&nbsp; Criminal Sentencing &nbsp;|&nbsp; Personal Injury and Civil Rights &nbsp;|&nbsp; Immigration &nbsp;|&nbsp; Fitness for Duty, SSD and Workers Comp &nbsp;|&nbsp; Sex-Offenders &nbsp;|&nbsp; IME and Neuropsychological Testing &nbsp;|&nbsp; Behind-the-Scenes Consulting on a Contingency Fee &nbsp;|&nbsp; Low-Price Initial Screening Evaluations &nbsp;|&nbsp; Therapy Services and Programs for Litigants</p>
    </section>

    <div class="fine-print">
      <strong>Fenwick and Ostrander, LLC.</strong> 2018 New York Licensed Psychologist Lic. # 047213 -<br>
      New Jersey Licensed Psychologist Lic. # 72K400915300
    </div>
  </div>
</body>
</html>
```